PSD website for property company

Please read the brief thoroughly.

We are looking for a new website for a property group that does property acquisitions, property development and property management.
They buy, build and lease core inner city industrial assets in Sydney, Australia.
They also invest in residential developments.

Site menu
- Home page
- Property – sub menus include – Leasing ; Projects ; Investments ; Property Management
- Capital and finance
- About
- Contact

They like this website
https://www.verlo.com.au/

They want the site to be clean, modern and bold.
They like few colors, even black and white is OK to submit

They have a logo and style guide and useable images here:
http://www.kumet.net/temp/PelorisWeb2019.zip
The zip file is also attached to this project.
We have supplied some images to give you an idea, but we will also require you to provide at least 3 extra images from stock photos.
Use your imagination.

I am expecting a lot of similar designs, so be aware the photos you choose will be really important.
They want really 3 good stock photos used and supplied without charge.
Please not too generic, I repeat the quality of the photos is important.
You may provide several photos (but not in multiple submissions please) and we will choose the best three to be provided.

The winner will be selected on a single home page design and required to provide;
All photos use in original format without charge
A second ‘standard page’ template design based on the winning home page design

```html
<!DOCTYPE html>
<html lang="en">
<head>
<meta charset="utf-8">
<title>Peloris — Industrial Property, Sydney</title>
<link rel="stylesheet" href="https://fonts.googleapis.com/css2?family=Roboto+Condensed:wght@300;400;700&family=Roboto:wght@300;400;500;700&display=swap">
<style>
:root{
  --green:#4e6a2e;
  --green-dark:#3f5823;
  --mint:#eef6e6;
  --mint-line:#d9e8c9;
  --ink:#1b1b1b;
  --night:#1e201c;
  --grey:#6d6d6d;
  --white:#ffffff;
}
*{box-sizing:border-box;margin:0;padding:0}
html,body{width:1200px;height:3333px;overflow:hidden}
body{position:relative;background:var(--white);font-family:"Roboto",Arial,sans-serif;color:var(--ink)}
.abs{position:absolute}
.cond{font-family:"Roboto Condensed","Arial Narrow",sans-serif}

/* header */
.site-header{position:absolute;left:0;top:0;width:1200px;height:85px;background:var(--white)}
.brand{position:absolute;left:36px;top:24px;font-family:"Roboto Condensed",sans-serif;font-weight:400;font-size:32px;letter-spacing:9px;color:var(--ink)}
.main-nav{position:absolute;left:430px;top:34px;display:flex;gap:26px;font-family:"Roboto Condensed",sans-serif;font-weight:700;font-size:11px;text-transform:uppercase;color:var(--ink)}
.main-nav .active{color:var(--green)}
.btn-contact{position:absolute;left:1071px;top:28px;width:89px;height:28px;border-radius:14px;background:var(--green);color:var(--white);font:700 10px "Roboto Condensed",sans-serif;display:flex;align-items:center;justify-content:center;text-transform:uppercase}

/* hero */
.hero{position:absolute;left:0;top:85px;width:1200px;height:515px;overflow:hidden}
.hero-photo{position:absolute;inset:0;background:linear-gradient(180deg,#5d6a73 0%,#7a7f7c 35%,#5b5e52 62%,#3f4a33 100%)}
.hero-shade{position:absolute;inset:0;background:rgba(20,22,18,.35)}
.hero h1{position:absolute;left:0;top:196px;width:1200px;text-align:center;color:var(--white);font:700 25px/1.2 "Roboto Condensed",sans-serif}
.btn-explore{position:absolute;left:522px;top:277px;width:156px;height:31px;border-radius:16px;background:var(--white);font:700 10px "Roboto Condensed",sans-serif;display:flex;align-items:center;padding-left:44px}
.btn-explore .ico{position:absolute;left:3px;top:3px;width:25px;height:25px;border-radius:50%;background:var(--green)}
.hero-dots{position:absolute;left:37px;top:226px}
.hero-dots span{display:block;width:4px;height:4px;border-radius:50%;background:#fff;margin-bottom:7px;opacity:.7}
.hero-dots span:first-child{width:8px;height:8px;margin-left:-2px;opacity:1}
.side-tabs{position:absolute;left:1140px;top:200px}
.side-tabs div{width:60px;height:54px;background:#8fb079;margin-bottom:4px;border-radius:8px 0 0 8px;display:flex;align-items:center;justify-content:center}
.hero-count{position:absolute;left:1118px;top:462px;color:#fff;font:700 13px "Roboto Condensed",sans-serif}
.hero-arrow{position:absolute;left:590px;top:458px}

/* section heading */
.sec-title{position:absolute;border-left:4px solid var(--green);padding-left:14px}
.sec-title h2{font:700 33px/1 "Roboto Condensed",sans-serif;text-transform:uppercase;color:var(--ink);margin-top:4px}
.sec-title p{font:300 25px/1.1 "Roboto Condensed",sans-serif;color:var(--green);margin-top:2px}
.on-dark h2,.on-dark p{color:var(--white)}

.btn-outline{position:absolute;border:2px solid var(--green);border-radius:18px;font:700 10px "Roboto Condensed",sans-serif;color:var(--ink);display:flex;align-items:center;justify-content:center;gap:8px;text-transform:uppercase;background:transparent}
.btn-outline.light{border-color:#fff;color:#fff}

/* featured */
.featured{position:absolute;left:0;top:600px;width:1200px;height:711px;background:var(--mint)}
.search-label{position:absolute;left:798px;top:72px;font:700 15px "Roboto Condensed",sans-serif;color:var(--green)}
.search-box{position:absolute;left:798px;top:100px;width:364px;height:36px;display:flex;border-radius:18px;overflow:hidden;background:#fff}
.search-box span{flex:1;font:400 10px "Roboto",sans-serif;color:#999;padding:13px 0 0 16px}
.search-box b{width:89px;background:var(--green);color:#fff;font:700 10px "Roboto Condensed",sans-serif;display:flex;align-items:center;justify-content:center}
.prop-photo{position:absolute;border-radius:6px 6px 0 0}
.prop-info{position:absolute;border-radius:6px;padding:16px 18px;background:#fff;box-shadow:0 4px 14px rgba(0,0,0,.08)}
.prop-info.dark{background:var(--green);color:#fff}
.prop-info h3{font:700 23px "Roboto Condensed",sans-serif;margin-bottom:10px}
.prop-info p{font:400 10.5px/1.55 "Roboto",sans-serif;color:#8a8a8a}
.prop-info.dark p{color:#e6eedc}
.prop-info .more{font:700 10px "Roboto Condensed",sans-serif;margin-top:12px;display:flex;align-items:center;gap:5px;color:var(--green)}
.prop-info.dark .more{color:#fff}

/* capital */
.capital{position:absolute;left:0;top:1311px;width:1200px;height:596px;background:#fff}
.cap-card{position:absolute;top:187px;width:289px}
.cap-photo{height:209px;position:relative}
.cap-photo .overlay{position:absolute;inset:0;background:rgba(78,106,46,.72);display:flex;align-items:center;justify-content:center;color:#fff;font:700 12px "Roboto Condensed",sans-serif;gap:6px}
.cap-facts{height:49px;background:var(--mint);display:flex;justify-content:space-around;align-items:center;font:400 9px "Roboto",sans-serif;color:#555;text-align:center;text-transform:uppercase}
.cap-facts svg{display:block;margin:0 auto 2px}
.cap-card h3{font:700 17px "Roboto Condensed",sans-serif;margin:22px 0 0 22px}
.cap-card .sub{font:400 10px "Roboto",sans-serif;color:#666;margin:8px 0 0 22px}
.cap-card .price{font:700 17px "Roboto Condensed",sans-serif;color:var(--green);margin:10px 0 0 22px}

/* about */
.about{position:absolute;left:0;top:1907px;width:1200px;height:511px;background:var(--green);overflow:hidden}
.about-photo{position:absolute;left:-178px;top:-122px;width:778px;height:778px;border-radius:50%;background:linear-gradient(160deg,#c9d8e6 0%,#9aa6ad 35%,#5e4a3c 60%,#3c3a33 100%)}
.about-lead{position:absolute;left:687px;top:182px;width:345px;font:700 15px/1.35 "Roboto Condensed",sans-serif;color:#fff}
.about-body{position:absolute;left:687px;top:265px;width:345px;font:400 10.5px/1.6 "Roboto",sans-serif;color:#e4ecd9}

/* contact form */
.touch{position:absolute;left:0;top:2418px;width:1200px;height:598px;background:var(--night);overflow:hidden}
.touch-bg{position:absolute;inset:0;background:linear-gradient(180deg,#2a2d27 0%,#1b1c19 100%)}
.field{position:absolute;left:162px;width:427px;height:40px;border-bottom:1px solid #6a6a64;font:700 11px "Roboto",sans-serif;color:#fff}
.pills{position:absolute;left:160px;top:453px;display:flex;gap:7px}
.pills span{height:26px;border:1px solid #cfcfcf;border-radius:13px;color:#fff;font:400 10px "Roboto",sans-serif;display:flex;align-items:center;justify-content:center}
.btn-submit{position:absolute;left:160px;top:506px;width:122px;height:33px;border-radius:17px;background:#fff;font:700 10px "Roboto Condensed",sans-serif;display:flex;align-items:center;justify-content:center}
.agent-photo{position:absolute;left:693px;top:118px;width:382px;height:382px;border-radius:50%;background:radial-gradient(circle at 50% 45%,#f4f4f4 0%,#e6e6e6 60%,#d9d9d9 100%)}

/* footer */
.site-footer{position:absolute;left:0;top:3016px;width:1200px;height:317px;background:#fff}
.foot-h{position:absolute;left:162px;top:60px;font:700 15px "Roboto Condensed",sans-serif}
.foot-links{position:absolute;left:160px;top:101px;display:grid;grid-template-columns:151px 149px 149px 149px;row-gap:9px;font:400 10px "Roboto",sans-serif;color:#333}
.foot-links span::before{content:"› ";color:var(--green)}
.contact-box{position:absolute;left:762px;top:62px;width:276px;height:111px;border:1px solid #ddd;text-align:center;padding-top:24px}
.contact-box h4{font:700 15px "Roboto Condensed",sans-serif}
.contact-box .tel{font:700 17px "Roboto Condensed",sans-serif;color:var(--green);margin-top:2px}
.contact-box .mail{font:400 11px "Roboto",sans-serif;margin-top:4px}
.rule{position:absolute;left:162px;width:876px;height:1px;background:#ddd}
.foot-brand{position:absolute;left:160px;top:218px;font-family:"Roboto Condensed",sans-serif;font-weight:400;font-size:30px;letter-spacing:8px}
.social{position:absolute;left:882px;top:224px;display:flex;gap:13px}
.social span{width:28px;height:28px;border-radius:50%;border:1px solid #ccc}
.social span:first-child{background:var(--green);border-color:var(--green)}
.copyright{position:absolute;left:162px;top:285px;font:400 10px "Roboto",sans-serif;color:#333}
</style>
</head>
<body>

<header class="site-header">
  <div class="brand">PELORIS</div>
  <nav class="main-nav">
    <span class="active">Home</span><span>Property</span><span>Capital &amp; Finance</span><span>About</span><span>Contact</span>
  </nav>
  <div class="btn-contact">Contact</div>
</header>

<section class="hero">
  <div class="hero-photo" role="img" aria-label="Inner-city industrial redevelopment with arched brick facades and landscaped courtyard"></div>
  <div class="hero-shade"></div>
  <h1>We Buy, Build &amp; Lease core inner City Industrial assets<br>in Sydney, Australia.</h1>
  <div class="btn-explore"><span class="ico"></span>Explore Our Projects</div>
  <div class="hero-dots"><span></span><span></span><span></span><span></span></div>
  <div class="side-tabs">
    <div><svg width="26" height="30" viewBox="0 0 26 30" fill="none" stroke="#fff" stroke-width="2"><rect x="3" y="3" width="12" height="25"/><rect x="15" y="11" width="8" height="17"/><path d="M7 8h4M7 13h4M7 18h4"/></svg></div>
    <div><svg width="30" height="22" viewBox="0 0 30 22" fill="none" stroke="#fff" stroke-width="2"><rect x="2" y="2" width="26" height="18"/><path d="M2 2l13 10L28 2"/></svg></div>
  </div>
  <svg class="hero-arrow" width="20" height="20" viewBox="0 0 20 20" fill="none" stroke="#fff" stroke-width="2"><path d="M10 2v15M4 11l6 6 6-6"/></svg>
  <div class="hero-count">01/04</div>
</section>

<section class="featured">
  <div class="sec-title" style="left:162px;top:51px;height:82px">
    <h2>Featured Properties</h2><p>Must see properties</p>
  </div>
  <div class="search-label">Search properties</div>
  <div class="search-box"><span>Enter Location or Postal Code</span><b>SEARCH</b></div>

  <div class="prop-photo" style="left:38px;top:211px;width:373px;height:244px;background:linear-gradient(180deg,#5b4f6a 0%,#8a6a66 40%,#3b3a34 100%)" role="img" aria-label="Townhouse development at dusk"></div>
  <div class="prop-info dark" style="left:60px;top:438px;width:324px;height:146px">
    <h3>Property Name</h3>
    <p>Lorem ipsum dolor sit amet, consectetur adipiscing elit, sed do eiusmod tempor incididunt ut labore et dolore magna aliqua. Ut enim ad minim veniam.</p>
    <div class="more">View Details <svg width="10" height="10"><circle cx="5" cy="5" r="5" fill="#fff"/></svg></div>
  </div>

  <div class="prop-photo" style="left:413px;top:180px;width:371px;height:242px;background:linear-gradient(180deg,#dfe6ec 0%,#b9aa98 50%,#6a4a37 100%)" role="img" aria-label="Brick terrace homes with arched windows"></div>
  <div class="prop-info" style="left:433px;top:411px;width:329px;height:145px">
    <h3>Property Name</h3>
    <p>Lorem ipsum dolor sit amet, consectetur adipiscing elit, sed do eiusmod tempor incididunt ut labore et dolore magna aliqua. Ut enim ad minim veniam.</p>
    <div class="more">View Details <svg width="10" height="10" fill="none" stroke="#4e6a2e" stroke-width="1.5"><circle cx="5" cy="5" r="4"/></svg></div>
  </div>

  <div class="prop-photo" style="left:789px;top:211px;width:373px;height:244px;background:linear-gradient(180deg,#b7c6d8 0%,#dfe3e6 50%,#8f9488 100%)" role="img" aria-label="Street of white residential townhouses"></div>
  <div class="prop-info" style="left:809px;top:438px;width:327px;height:146px">
    <h3>Property Name</h3>
    <p>Lorem ipsum dolor sit amet, consectetur adipiscing elit, sed do eiusmod tempor incididunt ut labore et dolore magna aliqua. Ut enim ad minim veniam.</p>
    <div class="more">View Details <svg width="10" height="10" fill="none" stroke="#4e6a2e" stroke-width="1.5"><circle cx="5" cy="5" r="4"/></svg></div>
  </div>

  <div class="btn-outline" style="left:518px;top:615px;width:162px;height:34px">View All Properties <span>›</span></div>
</section>

<section class="capital">
  <div class="sec-title" style="left:162px;top:60px;height:82px">
    <h2>Capital &amp; Finance</h2><p>Featured Capital</p>
  </div>
  <div class="btn-outline" style="left:949px;top:98px;width:89px;height:33px">View All <span>›</span></div>

  <article class="cap-card" style="left:162px">
    <div class="cap-photo" role="img" aria-label="Suburban family house" style="background:linear-gradient(180deg,#c3d6e6,#7b8a6a)"><div class="overlay">CLICK TO EXPLORE →</div></div>
    <div class="cap-facts">
      <div><svg width="18" height="10"><rect x="1" y="3" width="16" height="6" fill="none" stroke="#555"/></svg>2<br>Bedrooms</div>
      <div><svg width="18" height="10"><rect x="1" y="3" width="16" height="6" fill="none" stroke="#555"/></svg>2<br>Receptions</div>
      <div><svg width="18" height="10"><path d="M1 5h16v4H1z" fill="none" stroke="#555"/></svg>1<br>Bathrooms</div>
    </div>
    <h3>Capital Name Here</h3><div class="sub">2 Bedroom House in City Name Here</div><div class="price">$210,000</div>
  </article>

  <article class="cap-card" style="left:456px">
    <div class="cap-photo" role="img" aria-label="Single-storey family house with driveway" style="background:linear-gradient(180deg,#8fb6e0 0%,#b7c9b5 55%,#8d8f86 100%)"></div>
    <div class="cap-facts">
      <div><svg width="18" height="10"><rect x="1" y="3" width="16" height="6" fill="none" stroke="#555"/></svg>2<br>Bedrooms</div>
      <div><svg width="18" height="10"><rect x="1" y="3" width="16" height="6" fill="none" stroke="#555"/></svg>2<br>Receptions</div>
      <div><svg width="18" height="10"><path d="M1 5h16v4H1z" fill="none" stroke="#555"/></svg>1<br>Bathrooms</div>
    </div>
    <h3>Capital Name Here</h3><div class="sub">2 Bedroom House in City Name Here</div><div class="price">$210,000</div>
  </article>

  <article class="cap-card" style="left:749px">
    <div class="cap-photo" role="img" aria-label="Two-storey suburban house" style="background:linear-gradient(180deg,#5d8fd0 0%,#8c7b68 55%,#9a9890 100%)"></div>
    <div class="cap-facts">
      <div><svg width="18" height="10"><rect x="1" y="3" width="16" height="6" fill="none" stroke="#555"/></svg>2<br>Bedrooms</div>
      <div><svg width="18" height="10"><rect x="1" y="3" width="16" height="6" fill="none" stroke="#555"/></svg>2<br>Receptions</div>
      <div><svg width="18" height="10"><path d="M1 5h16v4H1z" fill="none" stroke="#555"/></svg>1<br>Bathrooms</div>
    </div>
    <h3>Capital Name Here</h3><div class="sub">2 Bedroom House in City Name Here</div><div class="price">$210,000</div>
  </article>
</section>

<section class="about">
  <div class="about-photo" role="img" aria-label="Modern brick mixed-use building on a street corner"></div>
  <div class="sec-title on-dark" style="left:687px;top:71px;height:80px;border-color:#fff">
    <h2>About Us</h2><p>Who We Are</p>
  </div>
  <p class="about-lead">Duis aute irure dolor in reprehenderit in voluptate velit esse cillum dolore eu fugiat nulla pariatur consectetur adipisci velit.</p>
  <p class="about-body">Sed ut perspiciatis unde omnis iste natus error sit voluptatem accusantium doloremque laudantium, totam rem aperiam, eaque ipsa quae ab illo inventore veritatis et quasi architecto beatae vitae dicta sunt explicabo. Nemo enim ipsam voluptatem quia voluptas sit aspernatur aut odit aut fugit, sed quia consequuntur magni dolores eos qui ratione voluptatem sequi nesciunt. Neque porro quisquam est, qui dolorem ipsum quia sed quia non numquam eius modi tempora incidunt.</p>
  <div class="btn-outline light" style="left:687px;top:420px;width:160px;height:31px">View All Properties <span>›</span></div>
</section>

<section class="touch">
  <div class="touch-bg" role="img" aria-label="Darkened view of an arched industrial building"></div>
  <div class="sec-title on-dark" style="left:162px;top:66px;height:76px;border-color:#fff">
    <h2>Get In Touch</h2><p>Keep Up to Date</p>
  </div>
  <div class="field" style="top:200px">First Name*</div>
  <div class="field" style="top:256px">Last Name*</div>
  <div class="field" style="top:312px">Email Address*</div>
  <div class="field" style="top:367px">Phone</div>
  <div class="field" style="top:422px;border:none">I'm Interested In</div>
  <div class="pills">
    <span style="width:100px">Latest News</span><span style="width:100px">Investing</span><span style="width:93px">Buying</span><span style="width:96px">Leasing</span>
  </div>
  <div class="btn-submit">SUBMIT</div>
  <div class="agent-photo" role="img" aria-label="Customer service representative with headset"></div>
</section>

<footer class="site-footer">
  <div class="foot-h">Properties for sale in</div>
  <div class="foot-links">
    <span>Property Name, City</span><span>Property Name, City</span><span>Property Name, City</span><span>Property Name, City</span>
    <span>Property Name, City</span><span>Property Name, City</span><span>Property Name, City</span><span>Property Name, City</span>
  </div>
  <div class="contact-box">
    <h4>Contact Us</h4>
    <div class="tel">123 456 7890</div>
    <div class="mail">property@peloris.com</div>
  </div>
  <div class="rule" style="top:204px"></div>
  <div class="foot-brand">PELORIS</div>
  <div class="social"><span></span><span></span><span></span><span></span></div>
  <div class="rule" style="top:270px"></div>
  <div class="copyright">Copyright © <span style="color:var(--green)">Peloris</span> | Privacy Policy | Terms &amp; Conditions</div>
</footer>

</body>
</html>
```